Business Card

I would like a business card with a picture of my husband and I that is unique and professional.

Industry/Entity Type

Business

Font styles to use
Serif

```html
<!DOCTYPE html>
<html lang="en">
<head>
<meta charset="utf-8">
<title>Business Card – Dana Whitfield</title>
<link href="https://fonts.googleapis.com/css2?family=Cinzel:wght@400;700&family=Great+Vibes&display=swap" rel="stylesheet">
<style>
  :root{
    --page:#ece9e4;
    --card:#ffffff;
    --band:#0d0d0d;
    --accent:#b3213a;
    --ink:#1c1c1c;
    --band-text:#f4f4f4;
    --mark:#c99a3a;
    --photo-light:#f7f7f7;
    --photo-mid:#a9a9a9;
    --photo-dark:#6e6e6e;
  }
  *{margin:0;padding:0;box-sizing:border-box}
  html,body{width:1200px;height:1014px;overflow:hidden;background:var(--page)}
  .stage{width:1200px;height:1014px;display:flex;justify-content:center;align-items:center;gap:70px}
  .card{width:380px;height:665px;background:var(--card);position:relative;box-shadow:0 10px 30px rgba(0,0,0,.18);overflow:hidden}
  .card-front .band{position:absolute;top:62px;left:0;right:0;height:108px;background:var(--band);text-align:center;padding-top:14px}
  .name{font-family:"Great Vibes",cursive;color:var(--accent);font-size:40px;line-height:1}
  .title{font-family:"Cinzel",serif;color:var(--band-text);font-size:15px;letter-spacing:1.5px;line-height:1.3;margin-top:4px}
  .contact{position:absolute;top:205px;left:40px;right:40px;text-align:center;font-family:"Cinzel",serif;color:var(--ink);font-size:14px;letter-spacing:1px;line-height:1.6}
  .contact p{margin:6px 0}
  .rule{display:block;width:100%;height:10px}
  .brand-mark{position:absolute;top:390px;left:70px;width:220px;height:150px;display:flex;flex-direction:column;align-items:center;justify-content:center;gap:12px}
  .brand-dot{width:78px;height:78px;border-radius:50%;background:var(--mark)}
  .brand-word{font-family:"Cinzel",serif;font-weight:700;font-size:22px;letter-spacing:2px;color:var(--ink)}
  .company{position:absolute;top:555px;left:30px;width:300px;text-align:center}
  .company-name{font-family:"Cinzel",serif;font-weight:700;font-size:12.5px;letter-spacing:1px;color:var(--ink);margin:5px 0 2px}
  .company-cross{font-family:"Cinzel",serif;font-size:11px;color:var(--ink);line-height:1;margin-bottom:3px}
  .card-back .photo{position:absolute;inset:0;background:linear-gradient(160deg,var(--photo-light) 0%,var(--photo-light) 25%,var(--photo-mid) 65%,var(--photo-dark) 100%)}
</style>
</head>
<body>
<main class="stage">
  <section class="card card-front">
    <div class="band">
      <div class="name">Dana Whitfield</div>
      <div class="title">Professional Mentorship<br>Strategist</div>
    </div>
    <div class="contact">
      <svg class="rule" viewBox="0 0 300 10" preserveAspectRatio="none"><line x1="8" y1="5" x2="292" y2="5" stroke="#1c1c1c" stroke-width="1"/><path d="M0 5l8-3v6z M300 5l-8-3v6z" fill="#1c1c1c"/></svg>
      <p>555-214-7730 Direct</p>
      <p>danawhitfield@example.com</p>
      <svg class="rule" viewBox="0 0 300 10" preserveAspectRatio="none"><line x1="8" y1="5" x2="292" y2="5" stroke="#1c1c1c" stroke-width="1"/><path d="M0 5l8-3v6z M300 5l-8-3v6z" fill="#1c1c1c"/></svg>
    </div>
    <div class="brand-mark">
      <span class="brand-dot"></span>
      <span class="brand-word">Whitfield</span>
    </div>
    <div class="company">
      <svg class="rule" viewBox="0 0 300 10" preserveAspectRatio="none"><line x1="8" y1="5" x2="292" y2="5" stroke="#1c1c1c" stroke-width="1"/><path d="M0 5l8-3v6z M300 5l-8-3v6z" fill="#1c1c1c"/></svg>
      <p class="company-name">Whitfield Leadership Development</p>
      <p class="company-cross">+</p>
      <svg class="rule" viewBox="0 0 300 10" preserveAspectRatio="none"><line x1="8" y1="5" x2="292" y2="5" stroke="#1c1c1c" stroke-width="1"/><path d="M0 5l8-3v6z M300 5l-8-3v6z" fill="#1c1c1c"/></svg>
    </div>
  </section>
  <section class="card card-back">
    <div class="photo" role="img" aria-label="Portrait photo of the couple in grey suits, smiling, on a white background"></div>
  </section>
</main>
</body>
</html>
```